Commercial Real Estate Property Sign

Design a 4' x 4' sign that pops. Refer to examples.

Must include the following information:
A space to list (For Sale, For Lease, Build-to-Suite or Available)
Brightvale,LLC
Commercial Real Estate
company website
My Name (Marcus Pellow)
My Phone #

Industry/Entity Type

Real Estate

```html
<!DOCTYPE html>
<html lang="en">
<head>
<meta charset="utf-8">
<title>Brightvale LLC – For Lease Sign</title>
<link rel="stylesheet" href="https://fonts.googleapis.com/css2?family=Barlow:wght@400;500;700&family=Montserrat:wght@800&display=swap">
<style>
  :root {
    --header-grey: #3a3a3a;
    --brand-orange: #e8650a;
    --ink: #1f1f1f;
    --white: #ffffff;
  }
  html, body {
    margin: 0;
    padding: 0;
    width: 1200px;
    height: 1200px;
    overflow: hidden;
  }
  .sign {
    position: relative;
    width: 1200px;
    height: 1200px;
    background: var(--brand-orange);
    font-family: "Barlow", sans-serif;
    color: var(--ink);
  }
  .sign-header {
    position: absolute;
    top: 0;
    left: 0;
    width: 1200px;
    height: 272px;
    background: var(--header-grey);
  }
  .company-name {
    position: absolute;
    top: 50px;
    left: 0;
    width: 100%;
    margin: 0;
    text-align: center;
    font-family: "Barlow", sans-serif;
    font-weight: 500;
    font-size: 104px;
    line-height: 1;
    color: var(--white);
  }
  .company-tagline {
    position: absolute;
    top: 172px;
    left: 0;
    width: 100%;
    display: flex;
    align-items: center;
    justify-content: center;
    gap: 24px;
    margin: 0;
    font-weight: 400;
    font-size: 44px;
    letter-spacing: 1px;
    line-height: 1;
    color: var(--white);
  }
  .tagline-rule {
    width: 260px;
    height: 3px;
    background: var(--brand-orange);
  }
  .listing-status {
    position: absolute;
    top: 400px;
    left: 0;
    width: 100%;
    margin: 0;
    text-align: center;
    font-family: "Montserrat", sans-serif;
    font-weight: 800;
    font-size: 178px;
    line-height: 1;
    letter-spacing: 2px;
    color: var(--white);
  }
  .agent-name {
    position: absolute;
    top: 712px;
    left: 0;
    width: 100%;
    margin: 0;
    text-align: center;
    font-weight: 400;
    font-size: 108px;
    line-height: 1;
  }
  .agent-phone {
    position: absolute;
    top: 832px;
    left: 0;
    width: 100%;
    margin: 0;
    text-align: center;
    font-weight: 700;
    font-size: 132px;
    line-height: 1;
    letter-spacing: 3px;
  }
  .company-website {
    position: absolute;
    top: 1056px;
    left: 0;
    width: 100%;
    display: flex;
    align-items: center;
    justify-content: center;
    gap: 20px;
    margin: 0;
    font-weight: 700;
    font-size: 82px;
    line-height: 1;
  }
  .globe-icon {
    width: 60px;
    height: 60px;
  }
</style>
</head>
<body>
  <main class="sign">
    <header class="sign-header">
      <p class="company-name">Brightvale LLC</p>
      <p class="company-tagline">
        <span class="tagline-rule"></span>
        Commercial Real Estate
        <span class="tagline-rule"></span>
      </p>
    </header>

    <h1 class="listing-status">FOR LEASE</h1>

    <p class="agent-name">Marcus Pellow</p>
    <p class="agent-phone">555.218.7390</p>

    <p class="company-website">
      <svg class="globe-icon" viewBox="0 0 40 40" aria-hidden="true">
        <g fill="none" stroke="#1f1f1f" stroke-width="3">
          <circle cx="20" cy="20" r="17"/>
          <ellipse cx="20" cy="20" rx="7.5" ry="17"/>
          <line x1="3" y1="20" x2="37" y2="20"/>
          <path d="M6 11 H34 M6 29 H34"/>
        </g>
      </svg>
      www.MyBrightvale.com
    </p>
  </main>
</body>
</html>
```